Etikett für Flaschenwein gesucht
Zielgruppe
Weingeschäft -> Verkauf von Flaschenweine; Zielgruppe: Weintrinker, Genusstrinker oder auch jene Personen, die beim Einkaufen einfach gerne eine Flasche Wein mitnehmen wollen und bewusst unsere Weinflasche wählen, da ihnen das Design der Etikette zusagt; !!! Folgeaufträge denkbar!!! für Weinkarten Design, Roll-Up, Autobeschriftungen u.v.m
Aufgabenstellung
Schlicht, elegant und modern; Entwurf einer Weinetikette für exclusive Weine, ev. auch mit dem Namen des Weinguts -> 'Fenzl' eine Marke/ein Logo gestalten bzw. soll auf der Etikette auf alle Fälle Name des Betriebs u. auch die Sorte z.b. 'Weinviertel DAC' ersichtlich sein.
Es gibt momentan Etiketten u. ein Logo aber auf Grund des Betriebsführer-Wechsels (alte Generation übergibt an die neue Generation) kann man hier unvoreingenommen kreativ sein, daher auch kein Upload von bestehenden Dateien.

```html
<!DOCTYPE html>
<html lang="de">
<head>
<meta charset="utf-8">
<title>Fenzl – Weinetiketten</title>
<link rel="stylesheet" href="https://fonts.googleapis.com/css2?family=Oswald:wght@700&family=UnifrakturMaguntia&family=Barlow+Condensed:wght@400;600&display=swap">
<style>
  :root {
    --page: #f4f4f4;
    --paper-light: #fbfdfb;
    --paper-dark: #1f1f1f;
    --brand-red: #f0444a;
    --signal-green: #22e33d;
    --ink-black: #0c0c0c;
    --poem-dark: #7a2424;
    --text-white: #f2f2f2;
    --butterfly-red: #d9433f;
  }
  html, body {
    margin: 0;
    padding: 0;
    width: 1200px;
    height: 2280px;
    overflow: hidden;
    background: var(--page);
  }
  .label-sheet {
    position: absolute;
    left: 110px;
    width: 980px;
    height: 1054px;
    display: block;
  }
  .label-sheet--veltliner { top: 60px; }
  .label-sheet--zweigelt { top: 1166px; }
  .brand-name {
    font-family: "Oswald", sans-serif;
    font-weight: 700;
  }
  .poem {
    font-family: "UnifrakturMaguntia", serif;
    font-size: 30px;
  }
  .poem-author {
    font-family: "UnifrakturMaguntia", serif;
    font-size: 28px;
    letter-spacing: 2px;
  }
  .wine-info {
    font-family: "Barlow Condensed", sans-serif;
    font-size: 18px;
    letter-spacing: 4px;
  }
  .wine-info--strong { font-weight: 600; }
  .winery-tag {
    font-family: "Barlow Condensed", sans-serif;
    font-size: 11px;
    letter-spacing: 3px;
  }
  .blend-multiply { mix-blend-mode: multiply; }
</style>
</head>
<body>

<!-- Grüner Veltliner label -->
<svg class="label-sheet label-sheet--veltliner" viewBox="0 0 555 597" xmlns="http://www.w3.org/2000/svg">
  <defs>
    <radialGradient id="wing-green" cx="50%" cy="45%" r="55%">
      <stop offset="0%" stop-color="#22e33d" stop-opacity="0.85"/>
      <stop offset="70%" stop-color="#22e33d" stop-opacity="0.45"/>
      <stop offset="100%" stop-color="#22e33d" stop-opacity="0"/>
    </radialGradient>
  </defs>
  <rect width="555" height="597" fill="var(--paper-light)"/>

  <text class="brand-name" x="80" y="300" font-size="330" textLength="400" lengthAdjust="spacingAndGlyphs" fill="var(--brand-red)" opacity="0.92">FENZL</text>

  <text class="winery-tag" x="0" y="0" fill="var(--brand-red)" transform="translate(68,4) rotate(90)">WEINGUT</text>

  <g class="poem blend-multiply" fill="var(--signal-green)">
    <text x="18" y="58">Der Nebel steigt, es fällt das Laub,</text>
    <text x="18" y="99">Schenk ein den Wein, den holden!</text>
    <text x="18" y="140">Wir wollen uns den grauen Tag</text>
    <text x="18" y="181">Vergolden, ja, vergolden!</text>
    <text x="18" y="222">Und geht es draußen noch so toll,</text>
    <text x="18" y="263">Unchristlich oder christlich,</text>
    <text x="18" y="304">Ist doch die Welt, die schöne Welt,</text>
    <text x="18" y="345">So gänzlich unverwüstlich!</text>
  </g>
  <text class="poem-author" x="535" y="384" text-anchor="end" fill="var(--signal-green)">Hallberg</text>

  <g role="img" aria-label="Illustration eines Schmetterlings in Grün">
    <ellipse cx="275" cy="495" rx="270" ry="95" fill="url(#wing-green)"/>
  </g>

  <g class="wine-info">
    <text x="60" y="455" class="wine-info--strong" fill="var(--brand-red)">GRÜNER VELTLINER</text>
    <text x="60" y="479" fill="var(--brand-red)">RIEDE LINDENFELD</text>
    <text x="60" y="503" class="wine-info--strong" fill="var(--brand-red)">2017</text>
    <text x="132" y="533" class="wine-info--strong" fill="var(--signal-green)">GRÜNER VELTLINER</text>
    <text x="132" y="557" fill="var(--signal-green)">RIEDE LINDENFELD</text>
    <text x="132" y="581" class="wine-info--strong" fill="var(--signal-green)">2017</text>
    <text x="400" y="557" fill="var(--signal-green)" letter-spacing="2">13,5% VOL</text>
  </g>
</svg>

<!-- Zweigelt label -->
<svg class="label-sheet label-sheet--zweigelt" viewBox="0 0 555 597" xmlns="http://www.w3.org/2000/svg">
  <defs>
    <radialGradient id="wing-red" cx="50%" cy="40%" r="55%">
      <stop offset="0%" stop-color="#d9433f" stop-opacity="0.8"/>
      <stop offset="65%" stop-color="#b8342f" stop-opacity="0.55"/>
      <stop offset="100%" stop-color="#8a2622" stop-opacity="0"/>
    </radialGradient>
  </defs>
  <rect width="555" height="597" fill="var(--paper-dark)"/>

  <g role="img" aria-label="Illustration eines Schmetterlings in Rot">
    <ellipse cx="278" cy="420" rx="275" ry="190" fill="url(#wing-red)"/>
  </g>

  <text class="brand-name" x="88" y="308" font-size="335" textLength="395" lengthAdjust="spacingAndGlyphs" fill="var(--ink-black)" opacity="0.93">FENZL</text>

  <text class="winery-tag" x="0" y="0" fill="#3a3a3a" transform="translate(72,4) rotate(90)">WEINGUT</text>

  <g class="poem" fill="var(--poem-dark)" opacity="0.6">
    <text x="18" y="58">Der Nebel steigt, es fällt das Laub,</text>
    <text x="18" y="99">Schenk ein den Wein, den holden!</text>
    <text x="18" y="140">Wir wollen uns den grauen Tag</text>
    <text x="18" y="181">Vergolden, ja, vergolden!</text>
    <text x="18" y="222">Und geht es draußen noch so toll,</text>
    <text x="18" y="263">Unchristlich oder christlich,</text>
    <text x="18" y="304">Ist doch die Welt, die schöne Welt,</text>
    <text x="18" y="345">So gänzlich unverwüstlich!</text>
  </g>
  <text class="poem-author" x="535" y="384" text-anchor="end" fill="var(--poem-dark)" opacity="0.6">Hallberg</text>

  <g class="wine-info" fill="var(--text-white)">
    <text x="62" y="455" class="wine-info--strong">ZWEIGELT</text>
    <text x="62" y="479">RIEDE LINDENFELD</text>
    <text x="62" y="503" class="wine-info--strong">2016</text>
    <text x="62" y="528">TROCKEN</text>
    <text x="375" y="531" letter-spacing="2">12,5% VOL</text>
    <text x="277" y="577" text-anchor="middle" font-size="17" letter-spacing="4.5" opacity="0.85">ÖSTERREICHISCHER QUALITÄTSWEIN</text>
  </g>
</svg>

</body>
</html>
```